Looking for an Innovative Print Design (Service Directory)

We need a new design for our advertisement within a printed colour services directory.

We are a compensation law firm called Velbrook Compensation Lawyers. Feel free to take a browse of our website www.velbrooklegal.com.au to get an idea of what we do and the kind of firm we are.

We are in the process of redeveloping our website and as such, so please don't adhere to the design principles of the current site- impress us with your originality!

On top of any editable formats, your final submissions must include a .pdf copy.
The same design will need to be presented in two dimensions:

- 154mm x 118mm (B1/B2 Half Page);
- 175mm x 113mm (B4 Half Page).

[For more information refer to attached Pdf.]

We have attached for you a few examples of other firms' designs (Sample1,2,3). These are by no means good, or what we're after, it's just to provide you with an idea of what sort of advertisements go into the service directory.

Hi all,

We want to emphasise that a priority of the design is that it must look:
• Professional
• Sophisticated
Please do not hesitate to use completely different colour schemes to the ones that are on our website- as we have said, our website will change in the near future, so cohesion between the current project and the website is not necessary!

Thanks!

Thank you for your submissions so far. There are some great ideas hidden in there. 

An issue we are having is that most of you are conforming to the same understanding of what it should look like. Remember that there is NO NEED to be bound by the image of firm as is. That is, feel free to use a different colour logo.

For inspiration, we relate well to the design aesthetics of: http://www.tinfernstudio.co.uk/

Look forward to seeing your 'out of the box' submissions. 

Reason: We've received a large amount of fantastic designs. However, what we're really looking for is something original. Please feel free to think outside the box (the final design doesn't need to look like a print ad), and construct a design that is completely incongruous with our website! While we do appreciate a minimalistic design, we have yet to receive something that really grabs your attention with its visuals. We're not sure but this may or may not be achieved with a full colour design. Thanks for all your submissions- they all have some features that really click with us. We look forward to the next wave of submissions!

Target Market(s)

We have various target markets, including mainly families, elderly people, blue collar workers.

These are individuals who are looking for assistance. They feel helpless or wronged.

Keep in mind that the people accessing these are those who prefer going to a printed directory rather than using a google search.

Industry/Entity Type

Law Firm

Font styles to use
Serif
Sans Serif

Requirements
Must have
• - Our name 'Velbrook Compensation Lawyers'
- Our logo (attached as logo.eps, logo.png, and logo.tif)
- Must include phone number as 1300 XXX XXX (this must be prominent)
- Must include the following service areas in these words: Motor vehicle claims, medical claims, superannuation claims, Workplace claims, negligence claims
- Our email address: info@velbrooklegal.com.au
- Our website address: www.velbrooklegal.com.au
- The following catchphrases: '98% success rate', and 'No win no fee' in those words
- Our location '412 Carvel Lane, Smithville, SYDNEY'
- For sizing dimensions, we need one in 154mm x 118mm and also a design in 175mm x 113mm (B4 Half Page) [refer to pdf attached]
Nice to have
• - Text indicating free initial consulatation
- Professional colour scheme
- As our website will be changed, do not worry about making the advertisement cohesive with our website design
- We want the design to be modern, but still professional
- Clean typeface
- No gradient colour scheme
- When designing, if you are looking to place more text onto the advertisement, these may be some considerations (feel free to change the wording): Accredited specialists, home and hospital visits

```html
<!DOCTYPE html>
<html lang="en">
<head>
<meta charset="utf-8">
<title>Velbrook Compensation Lawyers — Directory Advertisement</title>
<link rel="stylesheet" href="https://fonts.googleapis.com/css2?family=Montserrat:wght@300;600&family=Roboto+Condensed:wght@300;400;500;700&family=Roboto:wght@400&display=swap">
<style>
  :root {
    --paper: #ffffff;
    --navy: #023e5b;
    --sky: #7eaac5;
    --white: #ffffff;
  }
  * { margin: 0; padding: 0; box-sizing: border-box; }
  html, body { width: 1200px; height: 920px; overflow: hidden; background: var(--paper); }
  .ad {
    position: absolute; left: 30px; top: 30px; width: 1140px; height: 860px;
    background: var(--navy); color: var(--white);
    font-family: "Roboto Condensed", "Arial Narrow", sans-serif;
  }
  .brand-dot {
    position: absolute; left: 33px; top: 120px; width: 186px; height: 186px;
    border-radius: 50%; background: var(--sky);
  }
  .brand-name {
    position: absolute; left: 268px; top: 128px;
    font-family: "Montserrat", sans-serif; font-weight: 300;
    font-size: 104px; line-height: 1; letter-spacing: 6px; white-space: nowrap;
  }
  .brand-tagline {
    position: absolute; left: 274px; top: 255px;
    font-family: "Montserrat", sans-serif; font-weight: 600;
    font-size: 30px; line-height: 1; letter-spacing: 6.4px; white-space: nowrap;
  }
  .badge {
    position: absolute; left: 927px; top: 125px; width: 182px; height: 182px;
    border: 2px solid var(--sky); border-radius: 50%;
    display: flex; flex-direction: column; align-items: center; justify-content: center;
    text-align: center; line-height: 1;
  }
  .badge-figure { font-family: "Roboto", sans-serif; font-weight: 700; font-size: 36px; font-weight: 700; }
  .badge-label { font-weight: 300; font-size: 22px; margin-top: 8px; }
  .badge-terms { font-weight: 300; font-size: 18px; margin-top: 12px; }
  .badge-terms strong { font-weight: 700; }
  .rule { position: absolute; left: 32px; width: 1075px; height: 2px; background: var(--sky); }
  .rule--top { top: 331px; }
  .rule--bottom { top: 798px; }
  .services {
    position: absolute; left: 32px; top: 346px; width: 1075px;
    display: flex; justify-content: space-between; list-style: none;
    font-family: "Roboto", sans-serif; font-size: 18px; line-height: 22px; white-space: nowrap;
  }
  .services li + li::before { content: "|"; color: var(--sky); margin-right: 6px; }
  .offer {
    position: absolute; left: 0; top: 480px; width: 1140px;
    display: flex; align-items: center; justify-content: center; gap: 34px;
  }
  .offer-dot { width: 66px; height: 66px; border-radius: 50%; background: var(--white); flex: none; }
  .offer-title { font-weight: 400; font-size: 75px; line-height: 1; white-space: nowrap; }
  .offer-extras {
    position: absolute; left: 0; top: 578px; width: 1140px; text-align: center;
    color: var(--sky); font-weight: 500; font-size: 41px; line-height: 1; letter-spacing: 0.6px; white-space: nowrap;
  }
  .offer-extras .sep { color: var(--white); }
  .contact-main {
    position: absolute; left: 32px; top: 754px; width: 1075px;
    display: flex; justify-content: space-between; align-items: baseline;
    font-size: 42px; line-height: 1; white-space: nowrap;
  }
  .contact-name { font-weight: 300; letter-spacing: 1.2px; }
  .contact-name .sep { color: var(--sky); }
  .contact-phone { font-family: "Roboto", sans-serif; font-weight: 700; letter-spacing: 1px; }
  .contact-details {
    position: absolute; left: 32px; top: 809px; width: 1075px;
    font-family: "Roboto", sans-serif; font-size: 19px; line-height: 22px; white-space: nowrap;
    display: flex; justify-content: space-between;
  }
  .contact-details .sep { color: var(--sky); }
</style>
</head>
<body>
  <section class="ad">
    <div class="brand-dot"></div>
    <h1 class="brand-name">VELBROOK</h1>
    <p class="brand-tagline">COMPENSATION LAWYERS</p>

    <div class="badge">
      <span class="badge-figure">98%</span>
      <span class="badge-label">SUCCESS RATE</span>
      <span class="badge-terms">NO WIN <strong>NO FEE</strong></span>
    </div>

    <div class="rule rule--top"></div>
    <ul class="services">
      <li>MOTOR VEHICLE CLAIMS</li>
      <li>MEDICAL CLAIMS</li>
      <li>SUPERANNUATION CLAIMS</li>
      <li>WORKPLACE CLAIMS</li>
      <li>NEGLIGENCE CLAIMS</li>
    </ul>

    <div class="offer">
      <span class="offer-dot"></span>
      <h2 class="offer-title">FREE INITIAL CONSULTATION</h2>
      <span class="offer-dot"></span>
    </div>
    <p class="offer-extras">ACCREDITED SPECIALISTS <span class="sep">I</span> HOME AND HOSPITAL VISITS</p>

    <div class="contact-main">
      <span class="contact-name">VELBROOK COMPENSATION LAWYERS <span class="sep">I</span></span>
      <span class="contact-phone">1300 XXX XXX</span>
    </div>
    <div class="rule rule--bottom"></div>
    <p class="contact-details">
      <span>412 Carvel Lane, Smithville, SYDNEY</span><span class="sep">|</span>
      <span>info@velbrooklegal.com.au</span><span class="sep">|</span>
      <span>www.velbrooklegal.com.au</span>
    </p>
  </section>
</body>
</html>
```